New website for Pilates Studio

I need a new version of my website
http://bellwetherstretch.biz/
I want an updated fresh look with an easier to read schedule that looks good on mobile phones as well as laptops.
Clean, simple, fresh and BOLD

Target Market(s)

All ages, genders and races

Coding

Coded - Design and coding required

Number of Pages Required

4 page

Colors
9bcb3c

Requirements
Must have
• Photos that mostly use the real images from our studio. Browse our facebook page, website or ask me for high quality images

```html
<!DOCTYPE html>
<html lang="en">
<head>
<meta charset="utf-8">
<title>Bellwether Stretch – Pilates &amp; Rotary Studio</title>
<link rel="stylesheet" href="https://fonts.googleapis.com/css2?family=Arimo:wght@400;700&display=swap">
<style>
  :root {
    --green: #9bcb3c;
    --green-pale: #d7ecb8;
    --gold: #c99a2e;
    --gold-btn: #cf9f2f;
    --ink: #222222;
    --gray-band: #bdbdbd;
    --white: #ffffff;
  }
  * { box-sizing: border-box; margin: 0; padding: 0; }
  html, body { width: 1024px; height: 1200px; overflow: hidden; }
  body { position: relative; background: var(--white); font-family: "Arimo", Arial, sans-serif; color: var(--ink); }

  .topbar { position: absolute; left: 0; top: 0; width: 1024px; height: 40px; background: var(--green); color: var(--white); font-size: 12px; }
  .topbar__item { position: absolute; top: 0; height: 40px; display: flex; align-items: center; gap: 6px; }
  .topbar__address { left: 14px; }
  .topbar__email { left: 715px; }
  .topbar__phone { left: 922px; }

  .header { position: absolute; left: 0; top: 40px; width: 1024px; height: 91px; background: var(--green-pale); border-bottom: 1px solid var(--green); }
  .brand { position: absolute; left: 16px; top: 24px; }
  .brand__name { font-size: 30px; font-weight: 700; color: var(--green); letter-spacing: -0.5px; }
  .date-pill { position: absolute; right: 12px; top: 13px; background: var(--green); color: var(--white); font-size: 12px; padding: 5px 12px; border-radius: 10px; }
  .nav { position: absolute; right: 0; top: 61px; display: flex; list-style: none; }
  .nav__link { display: block; font-size: 12px; padding: 6px 16px; color: var(--ink); }
  .nav__link--active { background: var(--gold-btn); color: var(--white); border-radius: 6px 6px 0 0; }

  .hero { position: absolute; left: 0; top: 142px; width: 1024px; height: 378px; background: linear-gradient(180deg, #e9e4dc 0%, #c8b9a4 45%, #c08a4e 75%, #9b6a38 100%); border-bottom: 1px solid var(--green); }
  .hero__arrow { position: absolute; top: 166px; width: 44px; height: 44px; border-radius: 6px; background: var(--green); }
  .hero__arrow--prev { left: 22px; }
  .hero__arrow--next { left: 956px; }

  .welcome { position: absolute; left: 0; top: 521px; width: 1024px; height: 107px; text-align: center; }
  .welcome__title { margin-top: 15px; font-size: 24px; font-weight: 400; color: var(--gold); }
  .welcome__text { width: 740px; margin: 4px auto 0; font-size: 12px; line-height: 15px; }

  .features { position: absolute; left: 0; top: 628px; width: 1024px; height: 250px; background: var(--gray-band); }
  .feature { position: absolute; top: 25px; width: 321px; height: 202px; background: var(--white); border: 1px solid var(--green); text-align: center; }
  .feature--about { left: 9px; } .feature--schedule { left: 351px; } .feature--rates { left: 693px; }
  .feature__icon { display: block; margin: 10px auto 0; width: 108px; height: 108px; border-radius: 8px; background: var(--green); }
  .feature__title { margin-top: 10px; font-size: 18px; font-weight: 400; color: var(--green); }
  .feature__text { width: 290px; margin: 4px auto 0; font-size: 10px; line-height: 12px; }

  .section-title { position: absolute; top: 896px; font-size: 18px; font-weight: 400; color: var(--gold); border-bottom: 1px solid var(--green); padding-bottom: 3px; }
  .team-title { left: 10px; width: 662px; }
  .news-title { left: 693px; width: 321px; }

  .member { position: absolute; top: 931px; width: 200px; text-align: center; }
  .member--one { left: 10px; } .member--two { left: 241px; } .member--three { left: 472px; }
  .member__frame { height: 200px; background: var(--green); padding: 12px; }
  .member__photo { width: 176px; height: 176px; background: linear-gradient(180deg, #ece9e4 0%, #cdb8a6 50%, #6ec6e6 100%); }
  .member__name { margin-top: 2px; font-size: 14px; }

  .news { position: absolute; left: 693px; top: 934px; width: 321px; height: 202px; border: 1px solid var(--green); padding: 20px 0 0 23px; }
  .news__item + .news__item { margin-top: 26px; }
  .news__title { font-size: 14px; font-weight: 400; color: var(--green); }
  .news__meta { font-size: 10px; color: var(--gold); margin-left: 3px; }
  .news__text { margin-top: 5px; font-size: 10px; line-height: 12px; width: 280px; }

  .footer { position: absolute; left: 0; top: 1160px; width: 1024px; height: 40px; background: var(--green); color: var(--white); font-size: 14px; display: flex; align-items: center; padding-left: 15px; }
  .social { position: absolute; right: 14px; top: 8px; display: flex; gap: 20px; }
  .social__mark { width: 24px; height: 24px; border-radius: 50%; background: var(--white); }
</style>
</head>
<body>
  <div class="topbar">
    <span class="topbar__item topbar__address">
      <svg width="14" height="18" viewBox="0 0 14 18"><path d="M7 0a7 7 0 0 0-7 7c0 5 7 11 7 11s7-6 7-11a7 7 0 0 0-7-7z" fill="#fff"/><circle cx="7" cy="7" r="2.6" fill="#9bcb3c"/></svg>
      412 linden avenue #12&nbsp; Cedarbrook, CA 95110
    </span>
    <span class="topbar__item topbar__email">
      <svg width="24" height="16" viewBox="0 0 24 16"><rect x="1" y="1" width="22" height="14" fill="none" stroke="#fff" stroke-width="2"/><path d="M1 1l11 8 11-8" fill="none" stroke="#fff" stroke-width="2"/></svg>
      hello@bellwetherstretch.biz
    </span>
    <span class="topbar__item topbar__phone">
      <svg width="14" height="18" viewBox="0 0 14 18"><path d="M3 0l3 4-2 2c1 3 3 5 5 6l2-2 3 3-2 4C6 17 0 10 0 3z" fill="#fff"/></svg>
      555 014 2290
    </span>
  </div>

  <header class="header">
    <div class="brand">
      <span class="brand__name">Bellwether Stretch</span>
    </div>
    <span class="date-pill">FEBRUARY 14, 2015</span>
    <ul class="nav">
      <li><a class="nav__link nav__link--active">HOME</a></li>
      <li><a class="nav__link">SCHEDULE</a></li>
      <li><a class="nav__link">INSTRUCTORS</a></li>
      <li><a class="nav__link">RATES</a></li>
      <li><a class="nav__link">CONTACT</a></li>
    </ul>
  </header>

  <section class="hero" role="img" aria-label="Studio interior with rows of training machines on a wooden floor">
    <svg class="hero__arrow hero__arrow--prev" viewBox="0 0 44 44"><path d="M10 22l11-11v7h13v8H21v7z" fill="#fff"/></svg>
    <svg class="hero__arrow hero__arrow--next" viewBox="0 0 44 44"><path d="M34 22L23 11v7H10v8h13v7z" fill="#fff"/></svg>
  </section>

  <section class="welcome">
    <h1 class="welcome__title">WELCOME TO BELLWETHER STRETCH</h1>
    <p class="welcome__text">BELLWETHER STRETCH PILATES AND ROTARY STUDIO, IN THE HEART OF CEDAR VILLAGE, IS A WARM, INVITING STUDIO WHERE STUDENTS AND TEACHERS ALIKE ARE SUPPORTED AND ENCOURAGED TO DISCOVER AND GROW AT AN INDIVIDUAL PACE THROUGH THE FIELD OF INTEGRATED MOVEMENT.</p>
  </section>

  <section class="features">
    <article class="feature feature--about">
      <svg class="feature__icon" viewBox="0 0 108 108">
        <rect x="14" y="22" width="82" height="56" rx="6" fill="none" stroke="#fff" stroke-width="3"/>
        <rect x="8" y="30" width="82" height="56" rx="6" fill="#9bcb3c" stroke="#fff" stroke-width="3"/>
        <circle cx="32" cy="50" r="8" fill="none" stroke="#fff" stroke-width="3"/>
        <path d="M18 76c2-10 8-14 14-14s12 4 14 14" fill="none" stroke="#fff" stroke-width="3"/>
        <path d="M54 50h26M54 60h26M54 70h20" stroke="#fff" stroke-width="3"/>
      </svg>
      <h2 class="feature__title">ABOUT US</h2>
      <p class="feature__text">BELLWETHER PILATES AND ROTARY STUDIO, IN THE HEART OF CEDAR VILLAGE, IS A WARM, INVITING STUDIO WHERE STUDENTS AND TEACHERS ALIKE...</p>
    </article>
    <article class="feature feature--schedule">
      <svg class="feature__icon" viewBox="0 0 108 108">
        <rect x="12" y="18" width="72" height="66" rx="5" fill="none" stroke="#fff" stroke-width="3"/>
        <path d="M12 32h72M28 12v12M68 12v12" stroke="#fff" stroke-width="3"/>
        <g fill="#fff"><rect x="22" y="42" width="8" height="6"/><rect x="36" y="42" width="8" height="6"/><rect x="50" y="42" width="8" height="6"/><rect x="22" y="56" width="8" height="6"/><rect x="36" y="56" width="8" height="6"/><rect x="22" y="70" width="8" height="6"/></g>
        <circle cx="76" cy="78" r="20" fill="#9bcb3c" stroke="#fff" stroke-width="3"/>
        <path d="M76 66v13l8 6" fill="none" stroke="#fff" stroke-width="3"/>
      </svg>
      <h2 class="feature__title">SCHEDULE</h2>
      <p class="feature__text">BELLWETHER PILATES AND ROTARY STUDIO, IN THE HEART OF CEDAR VILLAGE, IS A WARM, INVITING STUDIO WHERE STUDENTS AND TEACHERS ALIKE...</p>
    </article>
    <article class="feature feature--rates">
      <svg class="feature__icon" viewBox="0 0 108 108">
        <circle cx="54" cy="54" r="38" fill="#fff"/>
        <circle cx="54" cy="54" r="28" fill="#9bcb3c"/>
        <path d="M64 42c-2-4-6-5-10-5-6 0-10 3-10 8 0 11 21 6 21 17 0 5-5 8-11 8-5 0-9-2-11-6M54 32v44" fill="none" stroke="#fff" stroke-width="5"/>
      </svg>
      <h2 class="feature__title">RATES</h2>
      <p class="feature__text">BELLWETHER PILATES AND ROTARY STUDIO, IN THE HEART OF CEDAR VILLAGE, IS A WARM, INVITING STUDIO WHERE STUDENTS AND TEACHERS ALIKE...</p>
    </article>
  </section>

  <h2 class="section-title team-title">OUR TEAM</h2>
  <h2 class="section-title news-title">NEWS &amp; EVENTS</h2>

  <div class="member member--one">
    <div class="member__frame"><div class="member__photo" role="img" aria-label="Portrait photo of instructor Marla Quent"></div></div>
    <p class="member__name">MARLA QUENT</p>
  </div>
  <div class="member member--two">
    <div class="member__frame"><div class="member__photo" role="img" aria-label="Portrait photo of instructor Marla Quent"></div></div>
    <p class="member__name">MARLA QUENT</p>
  </div>
  <div class="member member--three">
    <div class="member__frame"><div class="member__photo" role="img" aria-label="Portrait photo of instructor Marla Quent"></div></div>
    <p class="member__name">MARLA QUENT</p>
  </div>

  <section class="news">
    <article class="news__item">
      <h3 class="news__title">WE'RE GREEN CERTIFIED!</h3>
      <p class="news__meta">POSTED BY 14 FEB, 2015</p>
      <p class="news__text">BELLWETHER PILATES AND ROTARY STUDIO, IN THE HEART OF CEDAR VILLAGE, IS A WARM, INVITING STUDIO WHERE STUDENTS AND TEACHERS ALIKE...</p>
    </article>
    <article class="news__item">
      <h3 class="news__title">WE'RE GREEN CERTIFIED!</h3>
      <p class="news__meta">POSTED BY 14 FEB, 2015</p>
      <p class="news__text">BELLWETHER PILATES AND ROTARY STUDIO, IN THE HEART OF CEDAR VILLAGE, IS A WARM, INVITING STUDIO WHERE STUDENTS AND TEACHERS ALIKE...</p>
    </article>
  </section>

  <footer class="footer">
    COPYRIGHT @ ALL RIGHTS RESERVED.BELLWETHER STRETCH
    <div class="social">
      <span class="social__mark" role="img" aria-label="Social link"></span>
      <span class="social__mark" role="img" aria-label="Social link"></span>
      <span class="social__mark" role="img" aria-label="Social link"></span>
    </div>
  </footer>
</body>
</html>
```